Marrowdale Bowls Club - Hospitality Venue - Need a poster to advertise Drink Spcials

I am looking at promoting our drinks on special to promote via poster and social media. I have uploaded an example. Please change and make it original to our venue. I have added our club logos also.
Gullwing Coastal Ale Schooner $6.00
Cindermoor Valley Shiraz $8.50
Copper Hawk Stubbie $10.00
Bay Breeze Cocktail $10.00
Brackenfold Pear Cider  $5.00
Post Mix Jug $10.00
Please mention in fine print at the bottom.
The Marrowdale Bowls Club practices the Responsible Service of Alcohol. No Members discount apply to these prices

```html
<!DOCTYPE html>
<html lang="en">
<head>
<meta charset="utf-8">
<title>Special Drinks Menu – Marrowdale Bowls Club</title>
<link rel="stylesheet" href="https://fonts.googleapis.com/css2?family=Oswald:wght@500;600&family=Open+Sans:wght@400;600&family=Kaushan+Script&display=swap">
<style>
  :root {
    --backdrop: #666560;
    --board: #343435;
    --board-light: #3d3d3e;
    --gold: #c6a46c;
    --gold-deep: #a8864f;
    --chalk: #e9e9ea;
    --ink: #2b2b2c;
  }
  * { box-sizing: border-box; margin: 0; padding: 0; }
  html, body { width: 1200px; height: 2568px; overflow: hidden; }
  body { background: var(--backdrop); position: relative; }

  .menu-card {
    position: absolute; left: 60px; top: 520px;
    width: 1080px; height: 1527px;
    background: radial-gradient(ellipse at 50% 40%, var(--board-light), var(--board) 70%);
    box-shadow: 0 14px 30px rgba(0,0,0,.35);
    overflow: hidden;
    font-family: "Open Sans", sans-serif;
    text-align: center;
  }
  .dashed-frame {
    position: absolute; left: 50px; right: 50px; top: 42px; bottom: 45px;
    border: 3px dashed var(--gold);
  }
  .foliage {
    position: absolute; top: 0;
    background: linear-gradient(160deg, rgba(198,164,108,.85), rgba(198,164,108,0) 75%);
  }
  .foliage--left { left: 0; width: 390px; height: 270px; border-bottom-right-radius: 100%; }
  .foliage--right { right: 0; width: 250px; height: 250px; border-bottom-left-radius: 100%;
    background: linear-gradient(200deg, rgba(198,164,108,.85), rgba(198,164,108,0) 75%); }

  .block { position: absolute; left: 0; right: 0; }
  .venue-name {
    top: 180px; font-size: 50px; font-weight: 600; letter-spacing: 10px;
    color: var(--gold); line-height: 60px;
  }
  .title-script {
    top: 300px; font-family: "Kaushan Script", cursive; font-size: 120px;
    color: var(--gold); line-height: 140px; z-index: 2; transform: translateX(10px);
  }
  .title-main {
    top: 400px; font-family: "Oswald", sans-serif; font-weight: 600;
    font-size: 132px; line-height: 124px; color: var(--chalk); letter-spacing: 1px;
  }
  .ribbon {
    position: absolute; left: 305px; width: 470px; top: 529px; height: 45px;
    background: var(--gold);
    clip-path: polygon(0 0, 100% 0, 95% 50%, 100% 100%, 0 100%, 5% 50%);
    font-weight: 600; font-size: 30px; line-height: 45px; color: var(--ink);
  }

  .drinks-grid { position: absolute; left: 0; top: 0; width: 1080px; height: 1527px; }
  .grid-line { stroke: var(--gold-deep); stroke-width: 2; }

  .drink { position: absolute; width: 300px; }
  .drink__art {
    display: block; margin: 0 auto; width: 70px; height: 98px;
    background: linear-gradient(180deg, #f3efe6 0 22%, #e9a93a 22% 100%);
    border-radius: 10px 10px 6px 6px;
  }
  .drink__name {
    margin-top: 22px; font-weight: 600; font-size: 24px; line-height: 26px;
    color: var(--chalk); text-transform: uppercase;
  }
  .drink__price {
    margin-top: 6px; font-family: "Oswald", sans-serif; font-weight: 500;
    font-size: 38px; line-height: 46px; color: var(--gold);
  }
  .col-1 { left: 95px; } .col-2 { left: 395px; } .col-3 { left: 693px; }
  .row-1 { top: 637px; } .row-2 { top: 875px; }

  .fine-print {
    top: 1138px; font-size: 21px; line-height: 28px; color: var(--chalk);
    text-transform: uppercase; padding: 0 180px;
  }
  .club-name {
    top: 1250px; font-size: 32px; font-weight: 600; color: var(--gold); line-height: 44px;
  }
  .contact { top: 1362px; font-size: 26px; line-height: 36px; color: var(--gold); }
</style>
</head>
<body>
  <main class="menu-card">
    <div class="foliage foliage--left" role="img" aria-label="Gold leaf sprigs decorating the top-left corner"></div>
    <div class="foliage foliage--right" role="img" aria-label="Gold leaf sprigs decorating the top-right corner"></div>
    <div class="dashed-frame"></div>

    <div class="block venue-name">TOLLGATE</div>
    <div class="block title-script">Special</div>
    <h1 class="block title-main">DRINKS MENU</h1>
    <div class="ribbon">BEST DRINKS IN TOWN</div>

    <svg class="drinks-grid" width="1080" height="1527" aria-hidden="true">
      <line class="grid-line" x1="394" y1="623" x2="394" y2="1099"/>
      <line class="grid-line" x1="716" y1="623" x2="716" y2="1099"/>
      <line class="grid-line" x1="137" y1="861" x2="943" y2="861"/>
    </svg>

    <div class="drink col-1 row-1">
      <span class="drink__art" role="img" aria-label="Illustration of a frothy schooner of ale"></span>
      <p class="drink__name">Gullwing Coastal<br>Ale Schooner</p>
      <p class="drink__price">$6.00</p>
    </div>
    <div class="drink col-2 row-1">
      <span class="drink__art" role="img" aria-label="Illustration of a glass of red wine and a tumbler"></span>
      <p class="drink__name">Cindermoor<br>Valley Shiraz</p>
      <p class="drink__price">$8.50</p>
    </div>
    <div class="drink col-3 row-1">
      <span class="drink__art" role="img" aria-label="Illustration of a frothy beer mug"></span>
      <p class="drink__name">Copper Hawk<br>Stubbie</p>
      <p class="drink__price">$10.00</p>
    </div>
    <div class="drink col-1 row-2">
      <span class="drink__art" role="img" aria-label="Illustration of two cocktail glasses"></span>
      <p class="drink__name">Bay Breeze<br>Cocktail</p>
      <p class="drink__price">$10.00</p>
    </div>
    <div class="drink col-2 row-2">
      <span class="drink__art" role="img" aria-label="Illustration of a bottle of pear cider"></span>
      <p class="drink__name">Brackenfold<br>Pear Cider</p>
      <p class="drink__price">$5.00</p>
    </div>
    <div class="drink col-3 row-2">
      <span class="drink__art" role="img" aria-label="Illustration of two frothy jugs"></span>
      <p class="drink__name">Post Mix<br>Jug</p>
      <p class="drink__price">$10.00</p>
    </div>

    <p class="block fine-print">The Marrowdale Bowls Club practices the responsible service of alcohol. No members discount apply to these prices</p>
    <p class="block club-name">Marrowdale Bowls Club</p>
    <p class="block contact">03 9000 4821<br>27 Larkspur Street, Marrowdale VIC</p>
  </main>
</body>
</html>
```